Core Investment Strategy's Super Pie Chart

We need a one page visual explanation of an investment strategy we call "Core/Perimeter". This strategy emphasizes a "core" portfolio that will seldom change and "perimeter" investments that will change. Our investment management firm caters to wealthy individuals. We want to project an image of strength and reliability. At the same time, we are willing to explore new concepts. I have uploaded a PDF of my graphically-challenged assistant's attempt at creating the one page visual.

Industry/Entity Type

Investment

```html
<!DOCTYPE html>
<html lang="en">
<head>
<meta charset="utf-8">
<title>Core / Perimeter Portfolio</title>
<link rel="stylesheet" href="https://fonts.googleapis.com/css2?family=Cinzel:wght@400;500;600&display=swap">
<style>
  :root {
    --page: #ffffff;
    --panel-light: #f1f1f1;
    --panel-mid: #dcdcdc;
    --ink: #2f2f33;
    --purple: #524ea4;
    --purple-deep: #4a1d7c;
    --purple-line: #2f2b63;
    --gold: #fbb316;
    --gold-deep: #c98a1a;
    --green: #8cc63f;
    --green-deep: #006838;
    --orange: #fbad3f;
    --orange-deep: #f7941d;
    --tan: #c49a6c;
    --tan-deep: #5a4636;
    --white-ring: #ffffff;
    --white-ring-deep: #8c8c8f;
    --label-green: #2e9a3e;
    --label-orange: #f26a2e;
    --label-brown: #7a5230;
    --label-purple: #4b479c;
  }
  html, body {
    margin: 0;
    width: 1200px;
    height: 900px;
    overflow: hidden;
    background: var(--page);
  }
  .canvas { display: block; width: 1200px; height: 900px; }
  .title { font-family: 'Cinzel', serif; font-size: 40px; fill: var(--ink); letter-spacing: 1px; }
  .segment-label { font-family: 'Cinzel', serif; font-size: 16px; }
  .segment-label--core { fill: var(--label-green); }
  .segment-label--alt { fill: var(--label-orange); }
  .segment-label--active { fill: var(--label-brown); font-size: 14px; }
  .segment-label--other { fill: var(--ink); font-size: 26px; }
  .bond-label { font-family: 'Cinzel', serif; font-size: 20px; fill: var(--ink); }
  .equity-label { font-family: 'Cinzel', serif; font-size: 20px; fill: var(--label-purple); }
  .leader-gold { fill: none; stroke: var(--gold); stroke-width: 3; }
  .leader-purple { fill: none; stroke: var(--purple); stroke-width: 3; }
  .arrow-gold { fill: var(--gold); }
  .arrow-purple { fill: var(--purple); }
</style>
</head>
<body>
<svg class="canvas" viewBox="0 0 1200 900" xmlns="http://www.w3.org/2000/svg">
  <defs>
    <linearGradient id="panel-fill" x1="0" y1="0" x2="1" y2="1">
      <stop offset="0" stop-color="#e4e4e4"/>
      <stop offset="0.5" stop-color="#f3f3f3"/>
      <stop offset="1" stop-color="#dedede"/>
    </linearGradient>
  </defs>

  <!-- Backdrop panel -->
  <rect class="backdrop" x="37" y="165" width="1153" height="650" fill="url(#panel-fill)"/>

  <text class="title" x="628" y="214" text-anchor="middle">Core / Perimeter Portfolio</text>

  <!-- Perimeter ring -->
  <g class="perimeter-ring">
    <path d="M890 498 A262 262 0 0 1 631 757 L631 713 A218 218 0 0 0 846 498 Z" fill="var(--tan-deep)" transform="translate(0 12)"/>
    <path d="M625 757 A262 262 0 0 1 366 498 L410 498 A218 218 0 0 0 625 713 Z" fill="var(--white-ring-deep)" transform="translate(0 12)"/>
    <path d="M366 492 A262 262 0 0 1 625 233 L625 277 A218 218 0 0 0 410 492 Z" fill="var(--green)"/>
    <path d="M396 492 A232 232 0 0 1 625 263 L625 277 A218 218 0 0 0 410 492 Z" fill="var(--green-deep)"/>
    <path d="M631 233 A262 262 0 0 1 890 492 L846 492 A218 218 0 0 0 631 277 Z" fill="var(--orange)"/>
    <path d="M631 263 A232 232 0 0 1 860 492 L846 492 A218 218 0 0 0 631 277 Z" fill="var(--orange-deep)"/>
    <path d="M890 498 A262 262 0 0 1 631 757 L631 713 A218 218 0 0 0 846 498 Z" fill="var(--tan)"/>
    <path d="M625 757 A262 262 0 0 1 366 498 L410 498 A218 218 0 0 0 625 713 Z" fill="var(--white-ring)"/>
  </g>

  <!-- Core pie: extrusion -->
  <g class="pie-depth" transform="translate(0 14)">
    <path d="M628 320 A170 170 0 0 1 742 616 L648 512 A30 30 0 0 0 628 460 Z" fill="var(--purple-deep)"/>
    <path d="M742 616 A170 170 0 0 1 559 645 L616 517 A30 30 0 0 0 648 512 Z" fill="var(--purple-deep)"/>
    <path d="M559 645 A170 170 0 0 1 504 374 L606 470 A30 30 0 0 0 616 517 Z" fill="var(--gold-deep)"/>
  </g>

  <!-- Core pie: faces -->
  <g class="pie-equities" stroke="var(--purple-line)" stroke-width="2" stroke-linejoin="round">
    <path d="M628 320 A170 170 0 0 1 742 616 L648 512 A30 30 0 0 0 628 460 Z" fill="var(--purple)"/>
    <path d="M742 616 A170 170 0 0 1 694 647 L640 518 A30 30 0 0 0 648 512 Z" fill="var(--purple)"/>
    <path d="M694 647 A170 170 0 0 1 652 658 L632 520 A30 30 0 0 0 640 518 Z" fill="var(--purple)"/>
    <path d="M652 658 A170 170 0 0 1 559 645 L616 517 A30 30 0 0 0 632 520 Z" fill="var(--purple)"/>
  </g>
  <g class="pie-bonds" stroke="var(--gold-deep)" stroke-width="2" stroke-linejoin="round">
    <path d="M559 645 A170 170 0 0 1 504 374 L606 470 A30 30 0 0 0 616 517 Z" fill="var(--gold)"/>
    <path d="M504 374 A170 170 0 0 1 628 320 L628 460 A30 30 0 0 0 606 470 Z" fill="var(--gold)"/>
  </g>

  <!-- Segment labels -->
  <text class="segment-label segment-label--core" x="292" y="290">Attractive Core</text>
  <text class="segment-label segment-label--core" x="292" y="313">Assets,</text>
  <text class="segment-label segment-label--alt" x="830" y="294">Alternative Assets</text>
  <text class="segment-label segment-label--active" x="866" y="681">Actively Managed</text>
  <text class="segment-label segment-label--active" x="866" y="701">Mutual Funds</text>
  <text class="segment-label segment-label--other" x="328" y="705">Other</text>

  <!-- Bond leaders -->
  <polyline class="leader-gold" points="525,361 431,361 431,503 350,503"/>
  <polyline class="leader-gold" points="463,529 350,529"/>
  <path class="arrow-gold" d="M330 503 L342 495 L356 495 L344 503 L356 511 L342 511 Z"/>
  <path class="arrow-gold" d="M330 529 L342 521 L356 521 L344 529 L356 537 L342 537 Z"/>
  <text class="bond-label" x="120" y="510">Short Term Bonds</text>
  <text class="bond-label" x="120" y="539">Intermediate Bonds</text>

  <!-- Equity leaders -->
  <polyline class="leader-purple" points="790,480 910,480"/>
  <polyline class="leader-purple" points="736,614 797,614 797,512 910,512"/>
  <polyline class="leader-purple" points="692,645 830,645 830,545 910,545"/>
  <polyline class="leader-purple" points="605,660 605,705 853,705 853,583 910,583"/>
  <path class="arrow-purple" d="M930 480 L918 472 L904 472 L916 480 L904 488 L918 488 Z"/>
  <path class="arrow-purple" d="M930 512 L918 504 L904 504 L916 512 L904 520 L918 520 Z"/>
  <path class="arrow-purple" d="M930 545 L918 537 L904 537 L916 545 L904 553 L918 553 Z"/>
  <path class="arrow-purple" d="M930 583 L918 575 L904 575 L916 583 L904 591 L918 591 Z"/>
  <text class="equity-label" x="938" y="487">Lg Cap Equities</text>
  <text class="equity-label" x="938" y="519">Mid Cap Equities</text>
  <text class="equity-label" x="938" y="552">Sm Cap Equities</text>
  <text class="equity-label" x="938" y="590">Int'l/dev Cap Equities</text>
</svg>
</body>
</html>
```